Velvet Fern Beauty Bar Business Card

We need a modern, elegant business card design for our new beauty bar located in La Quinta, CA. The card should feel premium yet approachable, reflecting our brand identity: warm, stylish, and confidence-boosting.

Use our existing Velvet Fern Beauty Bar logo (to be provided as vector file).

Colors: Black, White, Blush / Nude accents, and Gold (metallic or foil effect if possible).

Typography: Clean sans-serif for clarity, with optional elegant script accent.
Design Style

Minimalist and modern with plenty of white space.

Premium look with a beauty/lifestyle feel (not overly corporate).

Option to explore vertical or horizontal orientation.

Rounded corners welcome, but not required.

Additional Notes

Design should print well in both matte and glossy finishes.

Please present mockups with both light and dark backgrounds.

Keep overall feel sleek, feminine, and high-end while still being approachable.

```html
<!DOCTYPE html>
<html lang="en">
<head>
<meta charset="UTF-8">
<title>Velvet Fern Beauty Bar – Business Card</title>
<link href="https://fonts.googleapis.com/css2?family=Montserrat:wght@400;500;700&display=swap" rel="stylesheet">
<style>
  :root {
    --stage: #2b2b2b;
    --card-dark: #232323;
    --card-light: #ffffff;
    --ink: #1a1a1a;
    --paper: #ffffff;
    --rule-dark: #cfcfcf;
  }
  * { box-sizing: border-box; margin: 0; padding: 0; }
  html, body { width: 1200px; height: 694px; overflow: hidden; }
  body {
    background: var(--stage);
    font-family: "Montserrat", sans-serif;
    display: flex;
    align-items: center;
    justify-content: center;
    gap: 60px;
  }
  .card {
    width: 500px;
    height: 286px;
    border-radius: 22px;
    position: relative;
    box-shadow: 0 18px 40px rgba(0,0,0,.45);
  }
  .card--front {
    background: var(--card-dark);
    color: var(--paper);
    display: flex;
    align-items: center;
    justify-content: center;
  }
  .brand {
    display: flex;
    flex-direction: column;
    align-items: center;
    gap: 8px;
  }
  .brand__tagline { font-size: 13px; font-weight: 400; letter-spacing: .5px; }
  .brand__name {
    display: flex; align-items: center; gap: 10px;
    font-size: 30px; font-weight: 500; letter-spacing: 1px;
    white-space: nowrap;
  }
  .brand__dot { width: 12px; height: 12px; border-radius: 50%; background: currentColor; flex: none; }
  .brand__rule { width: 240px; height: 1px; background: var(--rule-dark); }
  .card--back {
    background: var(--card-light);
    color: var(--ink);
  }
  .card--back .brand { position: absolute; top: 30px; right: 30px; align-items: flex-end; gap: 6px; }
  .card--back .brand__name { font-size: 22px; }
  .card--back .brand__tagline { font-size: 11px; }
  .card--back .brand__rule { width: 180px; background: var(--ink); }
  .divider { position: absolute; left: 30px; right: 30px; top: 118px; height: 1px; background: var(--ink); }
  .person { position: absolute; left: 30px; top: 132px; }
  .person__name { font-size: 22px; font-weight: 700; line-height: 1.2; }
  .person__role { font-size: 13px; font-weight: 400; margin-top: 2px; }
  .person__rule { display: block; width: 200px; height: 1px; background: var(--ink); margin: 10px 0; }
  .contacts { list-style: none; display: flex; flex-direction: column; gap: 6px; }
  .contacts li { display: flex; align-items: center; gap: 10px; font-size: 12.5px; }
  .contacts svg { width: 13px; height: 13px; flex: none; }
  .address {
    position: absolute; right: 30px; top: 150px;
    text-align: right; font-size: 12.5px; line-height: 1.6; font-style: normal;
  }
</style>
</head>
<body>
  <section class="card card--front">
    <div class="brand">
      <p class="brand__tagline">Soft Light, Bold You.</p>
      <p class="brand__name"><span class="brand__dot"></span>Velvet Fern Beauty Bar</p>
      <span class="brand__rule"></span>
    </div>
  </section>

  <section class="card card--back">
    <div class="brand">
      <p class="brand__tagline">Soft Light, Bold You.</p>
      <p class="brand__name"><span class="brand__dot"></span>Velvet Fern Beauty Bar</p>
      <span class="brand__rule"></span>
    </div>
    <span class="divider"></span>
    <div class="person">
      <p class="person__name">Daniel Reyes</p>
      <p class="person__role">Owner</p>
      <span class="person__rule"></span>
      <ul class="contacts">
        <li>
          <svg viewBox="0 0 24 24" aria-hidden="true"><path fill="currentColor" d="M6.6 10.8a15.1 15.1 0 0 0 6.6 6.6l2.2-2.2a1 1 0 0 1 1-.25 11.4 11.4 0 0 0 3.6.57 1 1 0 0 1 1 1V20a1 1 0 0 1-1 1A17 17 0 0 1 3 4a1 1 0 0 1 1-1h3.5a1 1 0 0 1 1 1c0 1.25.2 2.45.57 3.57a1 1 0 0 1-.25 1z"/></svg>
          044-987 654 321
        </li>
        <li>
          <svg viewBox="0 0 24 24" aria-hidden="true"><path fill="currentColor" d="M2 5h20v14H2zm2 2v.5l8 5 8-5V7z"/></svg>
          hello@velvetfern.com
        </li>
        <li>
          <svg viewBox="0 0 24 24" aria-hidden="true"><circle cx="12" cy="12" r="10" fill="none" stroke="currentColor" stroke-width="2"/><path d="M2 12h20M12 2c3 3 3 17 0 20M12 2c-3 3-3 17 0 20" fill="none" stroke="currentColor" stroke-width="1.6"/></svg>
          www.velvetfern.com
        </li>
      </ul>
    </div>
    <address class="address">
      78 Palm Grove Lane<br>
      92253, United States
    </address>
  </section>
</body>
</html>
```